Real Estate For Sale Signage

I'm an independent agent in Lismore NSW Australia with high standards and looking for a catching 'For Sale'sign board.
I like classy, elegant, stylish and simple best.
My colours are red, white and black.
I don't have a logo or other font designs I need to stick to. I like the concept of a house or real estate design.
Before I created this project I played around on publisher and created the PDF attached. I'm not sold on it, but I don't mind the way the name has been layed out. Originally I had a white background with black & red font.
Fancy fonts for my name would be nice, but must not be busy.
Updates

Just wanted to advise that I have updated my brief and used the tools available to help get my ideas through.

Thank you for your work and time.

Kind regards
Marella

Industry/Entity Type

Real Estate

Requirements
Must have
• For Sale
Marella Quint Real Estate (must stand out)
0400 517 382 (must stand out)
17 Tallowood Street North Lismore
www.marellaquintrealestate.com.au

```html
<!DOCTYPE html>
<html lang="en">
<head>
<meta charset="utf-8">
<title>Marella Quint Real Estate – For Sale Sign</title>
<link href="https://fonts.googleapis.com/css2?family=Arimo:wght@400&family=Crimson+Text:wght@400;600&family=Parisienne&display=swap" rel="stylesheet">
<style>
  :root {
    --ink: #0b0b0b;
    --ink-soft: #1c1c1c;
    --white: #ffffff;
    --silver: #b9b9b9;
    --red: #d90f12;
    --red-deep: #8e0608;
  }
  * { margin: 0; padding: 0; box-sizing: border-box; }
  html, body {
    width: 849px; height: 1200px; overflow: hidden;
    background: var(--white);
  }
  .sign {
    position: relative;
    width: 849px; height: 1200px;
    overflow: hidden;
  }
  .backdrop {
    position: absolute; inset: 0;
    background: radial-gradient(ellipse at 50% 45%, var(--ink-soft) 0%, var(--ink) 75%);
  }
  .headline {
    position: absolute; top: 22px; left: 0; width: 100%;
    text-align: center;
    font-family: "Arimo", Arial, sans-serif;
    font-weight: 400;
    font-size: 214px;
    line-height: 1;
    letter-spacing: 2px;
    background: linear-gradient(180deg, var(--white) 45%, var(--silver) 100%);
    -webkit-background-clip: text; background-clip: text;
    color: transparent;
  }
  .script {
    font-family: "Parisienne", cursive;
    color: var(--white);
  }
  .with {
    position: absolute; top: 300px; left: 0; width: 100%;
    text-align: center;
    font-size: 54px; line-height: 1;
  }
  .agency-name {
    position: absolute; top: 400px; left: 0; width: 100%;
    text-align: center;
    font-family: "Crimson Text", Georgia, serif;
    font-weight: 600;
    color: var(--white);
    font-size: 104px;
    line-height: 1.3;
  }
  .agency-mark {
    display: inline-block;
    width: 26px; height: 26px;
    border-radius: 50%;
    background: var(--red);
    vertical-align: middle;
    margin-right: 18px;
  }
  .phone {
    position: absolute; top: 846px; left: 14px;
    display: flex; align-items: baseline;
    color: var(--white);
  }
  .phone-label { font-size: 52px; margin-right: 4px; }
  .phone-number {
    font-family: "Crimson Text", Georgia, serif;
    font-weight: 400;
    font-size: 108px;
    line-height: 1;
    letter-spacing: 1px;
  }
  .contact-band {
    position: absolute; left: 8px; top: 945px;
    width: 826px; height: 255px;
    background: linear-gradient(180deg, var(--red) 0%, var(--red-deep) 100%);
  }
  .contact-text {
    position: absolute; left: 8px; width: 826px;
    font-family: "Crimson Text", Georgia, serif;
    font-weight: 600;
    color: var(--white);
    font-size: 43px;
    line-height: 1;
  }
  .website { top: 985px; text-align: center; }
  .address { top: 1080px; padding-left: 62px; }
</style>
</head>
<body>
  <main class="sign">
    <div class="backdrop" role="img" aria-label="Black background with a faint dark damask pattern"></div>

    <h1 class="headline">For Sale</h1>
    <p class="script with">with</p>

    <p class="agency-name"><span class="agency-mark"></span>Marella Quint<br>Real Estate</p>

    <p class="phone">
      <span class="script phone-label">phone</span>
      <span class="phone-number">0400-517-382</span>
    </p>

    <div class="contact-band" role="img" aria-label="Red band with a tonal red floral damask pattern"></div>
    <p class="contact-text website">www.marellaquintrealestate.com.au</p>
    <p class="contact-text address">17 Tallowood Street, North Lismore</p>
  </main>
</body>
</html>
```